Pig club info pack flyers

We need base artwork to which we can add headings and content. we are looking for double sided A4 designs with blank Word suitable blocks which can hold content on topics including the law, research findings, zoonotic diseases etc etc.
We want them bright but not too complex nor too cartoonish. they object is to be eye-catching but credible. Colours should reflect our logo colours. The running pig line art, if used, should be the yellow in our logo. Maybe a standard heading such as THE FACTS. Open to all ideas.
Target Market(s)
Potential members, existing members, land managers
Industry/Entity Type
Conservation/hunting

```html
<!DOCTYPE html>
<html lang="en">
<head>
<meta charset="utf-8">
<title>The Facts – Info Pack Flyer</title>
<link href="https://fonts.googleapis.com/css2?family=Tinos:wght@400;700&family=Montserrat:wght@500&display=swap" rel="stylesheet">
<style>
  :root {
    --brand-blue: #2f5cad;
    --brand-orange: #f2ae3a;
    --paper: #fdfdfd;
    --ink: #2b2b2b;
    --backdrop: #e4e4e4;
    --grass: #4f8f2a;
    --grass-light: #8cbf4a;
    --sky: #c9c3a6;
  }
  * { margin: 0; padding: 0; box-sizing: border-box; }
  html, body { width: 1200px; height: 945px; overflow: hidden; }
  body {
    background: var(--backdrop);
    font-family: "Tinos", "Times New Roman", serif;
    color: var(--ink);
  }
  .spread {
    position: absolute;
    top: 76px;
    left: 20px;
    display: flex;
    gap: 40px;
  }
  .flyer-page {
    position: relative;
    width: 560px;
    height: 792px;
    background: var(--paper);
    overflow: hidden;
  }
  .page-header, .page-footer {
    position: absolute;
    left: 0;
    width: 560px;
    display: block;
  }
  .page-header { top: 0; height: 111px; }
  .page-footer { bottom: 0; height: 80px; }
  .site-url {
    position: absolute;
    top: 24px;
    right: 39px;
    font-family: "Montserrat", Arial, sans-serif;
    font-weight: 500;
    font-size: 13px;
    color: #fff;
    letter-spacing: 0.2px;
  }
  .club-name {
    position: absolute;
    top: 80px;
    left: 30px;
    display: flex;
    align-items: center;
    gap: 6px;
    font-weight: 700;
    font-size: 13px;
    color: var(--brand-blue);
  }
  .club-name .dot {
    width: 14px;
    height: 14px;
    border-radius: 50%;
    background: var(--brand-blue);
  }
  .page-title {
    position: absolute;
    top: 104px;
    left: 0;
    width: 560px;
    text-align: center;
    font-weight: 400;
    font-size: 44px;
    color: var(--brand-blue);
    z-index: 2;
    letter-spacing: 0.5px;
  }
  .hero-photo {
    position: absolute;
    top: 129px;
    left: 40px;
    width: 480px;
    height: 233px;
    background: linear-gradient(to bottom, var(--sky) 0%, #a99b68 22%, var(--grass-light) 36%, var(--grass) 100%);
  }
  .body-text p {
    font-size: 10px;
    line-height: 12.5px;
    text-align: justify;
    margin-bottom: 12.5px;
  }
  .intro-block {
    position: absolute;
    top: 382px;
    left: 40px;
    width: 480px;
  }
  .column {
    position: absolute;
    width: 227px;
    overflow: hidden;
  }
  .front .column { top: 528px; height: 175px; }
  .back .column { top: 137px; height: 578px; }
  .column-left { left: 40px; }
  .column-right { left: 290px; }
  .running-boar {
    position: absolute;
    left: 413px;
    top: 718px;
    width: 119px;
    height: 48px;
    background: linear-gradient(90deg, rgba(242,174,58,0.35), rgba(242,174,58,0.15));
  }
</style>
</head>
<body>
<main class="spread">

  <!-- Front side -->
  <section class="flyer-page front">
    <svg class="page-header" viewBox="0 0 705 140" preserveAspectRatio="none" aria-hidden="true">
      <path d="M0 0 H705 V62 Q420 48 170 70 Q70 80 0 95 Z" fill="var(--brand-blue)"/>
      <path d="M150 80 Q450 56 705 82 V124 Q470 88 150 80 Z" fill="var(--brand-orange)"/>
    </svg>
    <span class="site-url">www.ridgefieldhunters.org.au</span>
    <div class="club-name"><span class="dot"></span>Ridgefield Hunters Club</div>

    <h1 class="page-title">THE FACTS</h1>
    <div class="hero-photo" role="img" aria-label="Photo of two pigs grazing on a green pasture with trees and hills behind"></div>

    <div class="intro-block body-text">
      <p>Lorem ipsum dolor sit amet, consectetur adipiscing elit. Suspendisse elit odio, egestas eu aliquam non, ullamcorper id purus. Pellentesque laoreet efficitur dolor ut tempus. Sed non nisl libero. Etiam laoreet mattis orci dictum porttitor. Vivamus vestibulum velit ac quam tempus, et tristique purus posuere. Donec et fringilla eros. Maecenas felis mauris, dapibus sagittis facilisis at, pulvinar lobortis augue. Mauris et dolor ut est egestas feugia.</p>
      <p>Fusce interdum tortor magna, lacinia aliquam lacus aliquam non. Proin quis tortor et sem suscipit rutrum. Nam sagittis mauris est, vitae interdum leo egestas sit amet. Sed posuere fermentum leo a vulputate. Interdum et malesuada fames ac ante ipsum primis in faucibus. Vestibulum sed bibendum nunc, eget tincidunt metus. Interdum et malesuada fames ac ante ipsum primis in faucibus. Donec suscipit congue tortor.</p>
    </div>

    <div class="column column-left body-text">
      <p>Lorem ipsum dolor sit amet, consectetur adipiscing elit. Suspendisse elit odio, egestas eu aliquam non, ullamcorper id purus. Pellentesque laoreet efficitur dolor ut tempus. Sed non nisl libero. Etiam laoeet mattis orci dictum porttitor. Vivamus vestibulum velit ac quam tempus, et tristique purus posuere. Donec et fringilla eros.</p>
      <p>Fusce interdum tortor magna, lacinia aliquam lacus aliquam non. Proin quis tortor et sem suscipit rutrum. Nam sagittis mauris est, vitae interdum leo egestas sit amet. Sed posuere fermentum leo a vulputate. Interdum et malesuada fames ac ante ipsum primis in faucibus. Vestibulum sed</p>
    </div>
    <div class="column column-right body-text">
      <p>bibendum nunc, eget tincidunt metus. Interdum et malesuada fames ac ante ipsum primis in faucibus. Donec suscipit congue tortor. Curabitur sodales aliquam dui id molestie. Sed sollicitudin aliquam risus, vitae efficitur sapien. Nullam ex dolor, bibendum sit amet dolor.itur justo scelerisque imperdiet.</p>
      <p>Praesent commodo ret enim sed egestas. Maecenas id auctor est, sed fringilla velit. Proin sed vestibulum nisl. Mauris sit amet ante dolor. Sed commodo bibendum augue, at accumsan eros dictum ut. Orci varius natoque penatibus et magnis dis parturient montes, nascetur ridiculus mus.</p>
    </div>

    <div class="running-boar" role="img" aria-label="Yellow line art of a running wild boar"></div>
    <svg class="page-footer" viewBox="0 0 705 100" preserveAspectRatio="none" aria-hidden="true">
      <path d="M0 40 Q350 26 705 88" fill="none" stroke="var(--brand-orange)" stroke-width="2.5"/>
      <path d="M0 68 Q360 52 705 94 V100 H0 Z" fill="var(--brand-orange)"/>
    </svg>
  </section>

  <!-- Back side -->
  <section class="flyer-page back">
    <svg class="page-header" viewBox="0 0 705 140" preserveAspectRatio="none" aria-hidden="true">
      <path d="M0 0 H705 V62 Q420 48 170 70 Q70 80 0 95 Z" fill="var(--brand-blue)"/>
      <path d="M150 80 Q450 56 705 82 V124 Q470 88 150 80 Z" fill="var(--brand-orange)"/>
    </svg>
    <span class="site-url">www.ridgefieldhunters.org.au</span>
    <div class="club-name"><span class="dot"></span>Ridgefield Hunters Club</div>

    <div class="column column-left body-text">
      <p>Lorem ipsum dolor sit amet, consectetur adipiscing elit. Suspendisse elit odio, egestas eu aliquam non, ullamcorper id purus. Pellentesque laoreet efficitur dolor ut tempus. Sed non nisl libero. Etiam laoeet mattis orci dictum porttitor. Vivamus vestibulum velit ac quam tempus, et tristique purus posuere. Donec et fringilla eros.</p>
      <p>Fusce interdum tortor magna, lacinia aliquam lacus aliquam non. Proin quis tortor et sem suscipit rutrum. Nam sagittis mauris est, vitae interdum leo egestas sit amet. Sed posuere fermentum leo a vulputate. Interdum et malesuada fames ac ante ipsum primis in faucibus. Vestibulum sed bibendum nunc, eget tincidunt metus. Interdum et malesuada fames ac ante ipsum primis in faucibus. Donec suscipit congue tortor. Curabitur sodales aliquam dui id molestie. Sed sollicitudin aliquam risus, vitae efficitur sapien. Nullam ex dolor, bibendum sit amet dolor.itur justo scelerisque imperdiet.</p>
      <p>Praesent commodo ret enim sed egestas. Maecenas id auctor est, sed fringilla velit. Proin sed vestibulum nisl. Mauris sit amet ante dolor. Sed commodo bibendum augue, at accumsan eros dictum ut. Orci varius natoque penatibus et magnis dis parturient montes, nascetur ridiculus mus.</p>
      <p>Lorem ipsum dolor sit amet, consectetur adipiscing elit. Suspendisse elit odio, egestas eu aliquam non, ullamcorper id purus. Pellentesque laoreet efficitur dolor ut tempus. Sed non nisl libero. Etiam laoreet mattis orci dictum porttitor. Vivamus vestibulum velit ac quam tempus, et tristique purus posuere. Donec et fringilla eros. Maecenas felis mauris, dapibus sagittis facilisis at, pulvinar lobortis augue. Mauris et dolor ut est egestas feugiat. Nulla vestibulum, risus a placerat imperdiet, ligula tortor pharetra odio, at finibus ex odio et lacus. Vivamus viverra sem nec auctor iaculis. Nunc ut porttitor risus.</p>
      <p>Fusce interdum tortor magna, lacinia aliquam lacus aliquam non. Proin quis tortor et sem suscipit rutrum. Nam sagittis mauris est, vitae interdum leo</p>
    </div>
    <div class="column column-right body-text">
      <p>egestas sit amet. Sed posuere fermentum leo a vulputate. Interdum et malesuada fames ac ante ipsum primis in faucibus. Vestibulum sed bibendum nunc, eget tincidunt metus. Interdum et malesuada fames ac ante ipsum primis in faucibus. Donec suscipit congue tortor. Curabitur sodales aliquam dui id molestie. Sed sollicitudin aliquam risus, vitae efficitur sapien. Nullam ex dolor, bibendum sit amet dolor in, cursus sollicitudin ligula. Orci varius natoque penatibus et magnis dis parturient montes, nascetur ridiculus mus. Duis faucibus aliquet risus, vel efficitur justo scelerisque imperdiet.</p>
      <p>Praesent commodo et enim sed egestas. Maecenas id auctor est, sed fringilla velit. Proin sed vestibulum nisl. Mauris sit amet ante dolor. Sed commodo bibendum augue, at accumsan eros dictum ut. Orci varius natoque penatibus et magnis dis parturient montes, nascetur ridiculus mus. Aenean varius dignissim bibendum. Duis sollicitudin nec mauris ullamcorper rutrum. In quis tempor enim, mollis tincidunt nibh. Duis gravida libero quis urna facilisis, euismod dictum enim blandit. Vestibulum sit amet tincidunt ligula.</p>
      <p>Phasellus vel dui dui. Sed blandit erat nec ex dapibus, et tempor sem gravida. Aliquam euismod tristique nisi, vitae consequat arcu placerat nec. Curabitur euismod ligula et velit rutrum, non viverra ipsum scelerisque. Integer nec sagittis dui, non tempus tellus. Duis sapien nisi, porttitor quis libero a, molestie porta risus. Vestibulum efficitur nisi magna, aliquet convallis mauris sollicitudin eget.</p>
      <p>Nunc nec fringilla ante, ut imperdiet dolor. Donec nec urna fringilla, malesuada tortor eu, placerat risus. Duis in accumsan dui. Maecenas eleifend feugiat sapien at varius. Nunc vitae scelerisque neque, quis pretium tellus. Pellentesque libero diam, mollis at elit non, pellentesque blandit leo. In in massa molestie, feugiat lorem non, dignissim nisi. Suspendisse eget augue commodo, hendrerit ligula id, facilisis massa. Aliquam viverra sit amet leo vel elementum.</p>
    </div>

    <div class="running-boar" role="img" aria-label="Yellow line art of a running wild boar"></div>
    <svg class="page-footer" viewBox="0 0 705 100" preserveAspectRatio="none" aria-hidden="true">
      <path d="M0 40 Q350 26 705 88" fill="none" stroke="var(--brand-orange)" stroke-width="2.5"/>
      <path d="M0 68 Q360 52 705 94 V100 H0 Z" fill="var(--brand-orange)"/>
    </svg>
  </section>

</main>
</body>
</html>
```